Small IT consulting firm needs a new web site

Quillmark Solutions, LLC is a company based out of Arizona with national presence. We work on both national, multinational, and international projects. We are Brindlesoft Partners. Heavy experience and work with Orbitline Control Kit, Vantra, Deskhub 720 . We offer Architecture, Design, Development, and implementation services. We have a specialty in Deskhub 720 migrations and implementations. We also have a specialized practice in Program and Project Management. The design message should foster a feeling of partnership and experience. Attached is my logo.

```html
<!DOCTYPE html>
<html lang="en">
<head>
<meta charset="utf-8">
<title>Quillmark Solutions, LLC</title>
<link href="https://fonts.googleapis.com/css2?family=Open+Sans:wght@400;600;700&family=Oswald:wght@400;500&display=swap" rel="stylesheet">
<style>
:root{
  --red:#c8161d;
  --red-dark:#a50f15;
  --ink:#333333;
  --muted:#777777;
  --dark:#3a3a3a;
  --darker:#262626;
  --band:#ececec;
  --line:#d6d6d6;
  --white:#ffffff;
  --blue:#1e88c9;
}
*{box-sizing:border-box;margin:0;padding:0}
html,body{width:839px;height:1200px;overflow:hidden}
body{font-family:"Open Sans",Arial,sans-serif;color:var(--ink);background:var(--white);position:relative}
.header{height:104px;position:relative}
.brand{position:absolute;left:48px;top:18px;display:flex;align-items:center;gap:10px}
.brand-mark{width:30px;height:30px;background:var(--red)}
.brand-name{font-family:"Oswald",sans-serif;font-size:22px;font-weight:500;color:var(--dark);line-height:1;letter-spacing:.5px}
.brand-sub{font-size:8px;color:var(--muted);letter-spacing:1px;margin-top:3px}
.contact{position:absolute;right:60px;top:20px;text-align:right;font-size:11px;line-height:17px}
.contact .call{color:var(--red);font-weight:700}
.contact .email{color:var(--muted);font-size:9px}
.nav{position:absolute;left:340px;right:60px;top:108px;height:22px;background:var(--darker);display:flex;align-items:center;font-size:9px;color:var(--white);font-weight:600}
.nav a{color:inherit;text-decoration:none;padding:0 14px;height:100%;display:flex;align-items:center}
.nav a.active{background:var(--red)}
.nav .search{margin-left:auto;margin-right:6px;width:100px;height:14px;background:var(--white);display:flex;justify-content:flex-end;align-items:center;padding-right:3px}
.hero{position:absolute;left:60px;right:60px;top:130px;height:245px;background:linear-gradient(120deg,#2c3137 0%,#5a6068 45%,#a7a9ab 70%,#3b3f45 100%)}
.hero .photo{position:absolute;inset:0}
.hero .arrow{position:absolute;top:112px;color:var(--white);font-size:20px;opacity:.7}
.caption{position:absolute;left:46px;top:80px;color:var(--white);width:210px}
.caption h2{font-weight:400;font-size:21px;margin-bottom:8px}
.caption p{font-size:8px;line-height:12px;opacity:.85;margin-bottom:10px}
.btn{display:inline-block;background:var(--white);color:var(--ink);font-size:8px;padding:4px 9px;font-weight:600}
.welcome{position:absolute;top:390px;left:60px;right:60px;text-align:center}
.welcome h1{font-size:19px;font-weight:700;color:var(--dark)}
.welcome h1 span{color:var(--red)}
.welcome .lead{font-size:9px;font-weight:700;margin:8px 0}
.welcome .body{font-size:8px;line-height:12px;color:var(--muted);padding:0 30px}
.partners{display:flex;justify-content:center;gap:48px;margin-top:20px;align-items:center;font-size:17px}
.partner{display:flex;align-items:center;gap:6px}
.partner .sq{width:16px;height:16px}
.p1{color:var(--red)}.p1 .sq{background:var(--red)}
.p2{color:var(--dark)}
.p3{color:var(--blue)}.p3 .sq{background:var(--blue)}
.offer{position:absolute;top:565px;left:0;right:0;height:250px;background:var(--band)}
.offer h2{text-align:center;font-weight:400;font-size:18px;margin-top:14px;color:var(--dark)}
.cards{display:flex;justify-content:center;gap:12px;margin-top:12px}
.card{width:135px;height:188px;background:var(--dark);color:var(--white);text-align:center;padding-top:18px}
.card.featured{background:var(--red)}
.card svg{width:40px;height:40px}
.card h3{font-size:11px;font-weight:700;margin:10px 0 5px}
.card p{font-size:7px;line-height:10px;padding:0 14px;opacity:.9}
.card .more{display:inline-block;margin-top:12px;background:var(--white);color:var(--ink);font-size:7px;font-weight:700;padding:3px 10px}
.request{position:absolute;top:815px;left:0;right:0;height:290px;background:#f4f4f4}
.request h2{text-align:center;font-size:16px;font-weight:600;margin-top:28px;color:var(--dark)}
.form{width:460px;margin:20px auto 0}
.row{display:flex;gap:10px}
.field{flex:1;height:16px;background:var(--white);border:1px solid var(--line);font-size:7px;color:var(--muted);padding:3px 5px}
.area{height:48px;margin-top:8px}
.submit{display:block;margin:8px auto 0;width:fit-content;background:var(--darker);color:var(--white);font-size:7px;font-weight:700;padding:4px 10px}
.footer{position:absolute;top:1105px;left:0;right:0;bottom:0;background:var(--darker);color:#bbbbbb;font-size:8px}
.footer .links{position:absolute;left:60px;top:30px;display:flex;gap:10px}
.footer .copy{position:absolute;left:60px;top:48px;font-size:7px}
.social{position:absolute;right:60px;top:32px;display:flex;gap:6px}
.social span{width:14px;height:14px;border-radius:50%;background:var(--blue)}
.social span:first-child{background:#3b5998}
</style>
</head>
<body>
<header class="header">
  <div class="brand">
    <div class="brand-mark"></div>
    <div>
      <div class="brand-name">QUILLMARK SOLUTIONS, LLC</div>
      <div class="brand-sub">WELCOME TO THE COMPANY</div>
    </div>
  </div>
  <div class="contact">
    <div class="call">Call : +1-480-555-0142</div>
    <div class="call">Toll Free : +1-888-555-0197</div>
    <div class="email">E-mail : hello@quillmarksolutions.co</div>
  </div>
  <nav class="nav">
    <a class="active">HOME</a><a>ABOUT US</a><a>SERVICES</a><a>CONTACT US</a>
    <div class="search"><svg width="8" height="8" viewBox="0 0 10 10"><circle cx="4" cy="4" r="3" fill="none" stroke="#555" stroke-width="1.4"/><line x1="6.3" y1="6.3" x2="9" y2="9" stroke="#555" stroke-width="1.4"/></svg></div>
  </nav>
</header>

<section class="hero">
  <div class="photo" role="img" aria-label="Team of consultants meeting around a table in a bright office"></div>
  <span class="arrow" style="left:10px">&#8249;</span>
  <span class="arrow" style="right:10px">&#8250;</span>
  <div class="caption">
    <h2>Aenean placerat nibh</h2>
    <p>Integer lacinia felis a nunc tempus, sed dictum justo porta. Curabitur et orci vitae metus varius.</p>
    <span class="btn">Read more</span>
  </div>
</section>

<section class="welcome">
  <h1>WELCOME TO <span>QUILLMARK SOLUTIONS</span></h1>
  <p class="lead">Phasellus blandit quam a ipsum gravida dapibus. Suspendisse elit ligula, iaculis dignissim justo eu, vestibulum venenatis elit.</p>
  <p class="body">Aenean sed quam non sapien faucibus consequat vitae sit amet erat. Praesent quis risus mi. In mollis nullam pulvinar dictum. Vivamus bibendum sagittis felis, ut dapibus ligula feugiat at. Ut dictum sapien nec tellus finibus fermentum. Integer faucibus lacus ut mollis venenatis. Donec posuere lorem nec massa ullamcorper id. Fusce ut tristique tortor, vel tempus tellus. Nunc feugiat mauris eget turpis tincidunt, at ornare nisi porta.</p>
  <div class="partners">
    <div class="partner p1"><span class="sq"></span>Deskhub 720</div>
    <div class="partner p2">Orbitline Control Kit</div>
    <div class="partner p3"><span class="sq"></span>Vantra</div>
  </div>
</section>

<section class="offer">
  <h2>We Offer</h2>
  <div class="cards">
    <div class="card featured">
      <svg viewBox="0 0 40 40" fill="#fff"><polygon points="20,4 36,13 4,13"/><rect x="7" y="15" width="4" height="15"/><rect x="15" y="15" width="4" height="15"/><rect x="23" y="15" width="4" height="15"/><rect x="31" y="15" width="4" height="15"/><rect x="4" y="32" width="32" height="4"/></svg>
      <h3>ARCHITECTURE</h3>
      <p>Nullam pharetra dolor nec ut, posuere tellus et mi. Mauris aliquet velit a metus.</p>
      <span class="more">MORE</span>
    </div>
    <div class="card">
      <svg viewBox="0 0 40 40" fill="#fff"><polygon points="33,3 37,7 20,24 16,20"/><path d="M14 22 L18 26 C18 32 12 36 5 35 C9 32 8 25 14 22Z"/></svg>
      <h3>DESIGN</h3>
      <p>Nullam pharetra dolor nec ut, posuere tellus et mi. Mauris aliquet velit a metus.</p>
      <span class="more">MORE</span>
    </div>
    <div class="card">
      <svg viewBox="0 0 40 40" fill="#fff"><path d="M28 4a9 9 0 0 0-8 12L5 31l4 4 15-15a9 9 0 0 0 12-8l-6 3-4-4 3-6z"/></svg>
      <h3>DEVELOPMENT</h3>
      <p>Nullam pharetra dolor nec ut, posuere tellus et mi. Mauris aliquet velit a metus.</p>
      <span class="more">MORE</span>
    </div>
    <div class="card">
      <svg viewBox="0 0 40 40" fill="none" stroke="#fff"><circle cx="15" cy="22" r="7" stroke-width="6" stroke-dasharray="3 2.5"/><circle cx="15" cy="22" r="3" stroke-width="2"/><circle cx="30" cy="10" r="5" stroke-width="4" stroke-dasharray="2.5 2"/></svg>
      <h3>IMPLEMENTATION</h3>
      <p>Nullam pharetra dolor nec ut, posuere tellus et mi. Mauris aliquet velit a metus.</p>
      <span class="more">MORE</span>
    </div>
  </div>
</section>

<section class="request">
  <h2>REQUEST INFORMATION</h2>
  <div class="form">
    <div class="row"><div class="field">Name</div><div class="field">E-mail</div><div class="field">Phone</div></div>
    <div class="field area">Message</div>
    <span class="submit">SUBMIT</span>
  </div>
</section>

<footer class="footer">
  <div class="links"><span>Home</span><span>|</span><span>About us</span><span>|</span><span>Services</span><span>|</span><span>Contact us</span></div>
  <div class="copy">Copyright &copy; 2015 Quillmark Solutions. All rights reserved.</div>
  <div class="social"><span></span><span></span><span></span></div>
</footer>
</body>
</html>
```